design a gift card and hanger backing for our saddlery

need a design for a pvc gift card (business card size) for our saddlery and if possible a back card board hanger. front to have a nice design and 'Gift Card' back of card to have our details supplied below. i will upload some pictures and logos but happy for them to be or not be used open to suggestions for designs

Target Market(s)

horse lovers of all ages and disaplines

Industry/Entity Type

Equestrian Supplies/Retail

Contact Information for Business Card

on the back - Thornvale Horse Supplies www.thornvales.net.au 1300 42 87 36 -and a signature panel (we will stick a code here)

Requirements
Must have
• horse themed
Nice to have
• open to all ideas
Should not have
• logo as main picture or on front

```html
<!DOCTYPE html>
<html lang="en">
<head>
<meta charset="utf-8">
<title>Thornvale Horse Supplies – Gift Card</title>
<link href="https://fonts.googleapis.com/css2?family=Montserrat:wght@500;800&family=Poppins:wght@400;500&family=Great+Vibes&display=swap" rel="stylesheet">
<style>
  :root{
    --stage:#2a2a2a;
    --navy:#24346b;
    --navy-deep:#1f2c5e;
    --rug:#5a3a80;
    --gold:#f6ad1b;
    --white:#ffffff;
    --ink:#1d2a66;
    --mist:#ececef;
  }
  *{margin:0;padding:0;box-sizing:border-box}
  html,body{width:1200px;height:800px;overflow:hidden;background:var(--stage)}
  .canvas{position:relative;width:1200px;height:800px}
  .card{
    position:absolute;width:540px;height:310px;border-radius:22px;overflow:hidden;
    border-bottom:3px solid var(--gold);
  }
  /* front */
  .card--front{left:50px;top:110px;background:var(--navy)}
  .front-photo{
    position:absolute;inset:0;
    background:
      radial-gradient(ellipse 34% 36% at 66% 44%, rgba(120,60,140,.7), transparent 72%),
      radial-gradient(ellipse 22% 30% at 24% 58%, rgba(95,80,130,.5), transparent 72%),
      linear-gradient(135deg,var(--navy) 0%,var(--navy-deep) 100%);
  }
  .gift-title{
    position:absolute;left:40px;top:54px;
    font-family:"Montserrat",sans-serif;font-weight:800;font-size:46px;letter-spacing:4px;
    line-height:1;color:var(--white);
  }
  .gift-rule{position:absolute;left:42px;top:116px;width:90px;height:4px;border-radius:2px;background:var(--gold)}
  .gift-tagline{
    position:absolute;left:40px;top:134px;width:240px;
    font-family:"Poppins",sans-serif;font-size:15px;line-height:1.4;color:var(--white);opacity:.85;
  }
  .brand{position:absolute;display:flex;align-items:center;gap:12px}
  .brand__dot{border-radius:50%;background:var(--gold);flex:none}
  .brand__name{font-family:"Poppins",sans-serif;font-weight:500;line-height:1.15}
  .card--front .brand{left:40px;bottom:32px}
  .card--front .brand__dot{width:30px;height:30px}
  .card--front .brand__name{color:var(--white);font-size:15px}
  /* back */
  .card--back{left:610px;top:380px;background:var(--white)}
  .back-ornament{
    position:absolute;left:150px;top:16px;width:260px;height:200px;border-radius:50%;
    background:radial-gradient(ellipse at center,var(--mist) 0%,rgba(236,236,239,0) 70%);
  }
  .card--back .brand{left:34px;top:160px}
  .card--back .brand__dot{width:48px;height:48px}
  .card--back .brand__name{color:var(--ink);font-size:19px}
  .back-title{
    position:absolute;left:270px;top:46px;width:250px;
    font-family:"Montserrat",sans-serif;font-weight:800;font-size:20px;line-height:1.15;color:var(--ink);
  }
  .contact{position:absolute;left:270px;top:110px;list-style:none}
  .contact__item{display:flex;align-items:center;gap:10px;margin-bottom:10px;
    font-family:"Poppins",sans-serif;color:var(--ink)}
  .contact__phone{font-size:17px;font-weight:500}
  .contact__web{font-size:14px}
  .contact__icon{width:24px;height:24px;border-radius:6px;background:var(--gold);display:flex;align-items:center;justify-content:center}
  .signature{position:absolute;right:36px;top:205px;font-family:"Great Vibes",cursive;font-size:30px;line-height:1;color:var(--ink)}
  .code{position:absolute;left:34px;bottom:30px;font-family:"Montserrat",sans-serif;font-weight:500;
    font-size:17px;letter-spacing:6px;color:var(--ink)}
</style>
</head>
<body>
<main class="canvas">
  <section class="card card--front" aria-label="Gift card front">
    <div class="front-photo" role="img" aria-label="Faded photo of a horse wearing a purple rug under a navy overlay"></div>
    <h2 class="gift-title">GIFT CARD</h2>
    <span class="gift-rule"></span>
    <p class="gift-tagline">For horse lovers of every age and discipline</p>
    <div class="brand">
      <span class="brand__dot"></span>
      <span class="brand__name">Thornvale Horse Supplies</span>
    </div>
  </section>

  <section class="card card--back" aria-label="Gift card back">
    <div class="back-ornament" role="img" aria-label="Faint decorative horse head ornament"></div>
    <div class="brand">
      <span class="brand__dot"></span>
      <span class="brand__name">Thornvale<br>Horse Supplies</span>
    </div>
    <h1 class="back-title">THORNVALE HORSE SUPPLIES</h1>
    <ul class="contact">
      <li class="contact__item">
        <span class="contact__icon">
          <svg width="14" height="14" viewBox="0 0 24 24"><path fill="#fff" d="M6.6 10.8a15 15 0 0 0 6.6 6.6l2.2-2.2c.3-.3.7-.4 1-.2 1.1.4 2.3.6 3.6.6.6 0 1 .4 1 1V20c0 .6-.4 1-1 1A17 17 0 0 1 3 4c0-.6.4-1 1-1h3.5c.6 0 1 .4 1 1 0 1.3.2 2.5.6 3.6.1.3 0 .7-.2 1z"/></svg>
        </span>
        <span class="contact__phone">1300 42 87 36</span>
      </li>
      <li class="contact__item">
        <span class="contact__icon">
          <svg width="14" height="14" viewBox="0 0 24 24" fill="none" stroke="#fff" stroke-width="2"><circle cx="12" cy="12" r="9"/><path d="M3 12h18M12 3c3 3 3 15 0 18M12 3c-3 3-3 15 0 18"/></svg>
        </span>
        <span class="contact__web">www.thornvales.net.au</span>
      </li>
    </ul>
    <p class="signature">Signature...</p>
    <p class="code">CODE.152368</p>
  </section>
</main>
</body>
</html>
```